Global Nano Technology Surface Protection company needs a new logo and cards

We are a Global company that will apply nanotechnology coatings on surfaces to prevent growth and spread of bacteria, viruses, mold etc. We deal with large corporates, airlines, hospitals and schools so we are after a new modern, simple and clean look that will have great visual impact.
We a company that is focused on prevention and protection.

Company name, Quorvane Systems Worldwide

Subtext, Antimicrobial Surface Protection

Logo, QVSW or QSW

Target Market(s)

Hospitals, Transport agencies, Airlines, Corporate entities

Industry/Entity Type

Protection

Contact Information for Business Card

Logo, QVSW or QSW
www.qvsw-example.us
Derek Holloway
+64290536218
tidyshieldnz@mailbox-example.com

Logo Text

QVSW

Requirements
Must have
• Simple clean look
Should not have
• Nothing too messy

```html
<!DOCTYPE html>
<html lang="en">
<head>
<meta charset="utf-8">
<title>Quorvane Systems Worldwide — Business Cards</title>
<link rel="stylesheet" href="https://fonts.googleapis.com/css2?family=Montserrat:wght@500;600&family=Open+Sans:wght@400&display=swap">
<style>
  :root {
    --backdrop: #ecebe8;
    --card-dark-center: #2a2e38;
    --card-dark-edge: #15181e;
    --card-light-center: #ffffff;
    --card-light-edge: #eeeff1;
    --brand-purple: #a21ee6;
    --brand-violet: #7a1ee6;
    --ink-white: #ffffff;
    --ink-grey: #4b4b4d;
    --ink-grey-soft: #555557;
  }
  * { margin: 0; padding: 0; box-sizing: border-box; }
  html, body {
    width: 1200px; height: 1200px; overflow: hidden;
    background: var(--backdrop);
  }
  .canvas { position: relative; width: 1200px; height: 1200px; }

  .card {
    position: absolute; left: 212px; width: 778px; height: 444px;
    box-shadow: 0 10px 28px rgba(0,0,0,0.18);
    overflow: hidden;
  }
  .card--front {
    top: 140px;
    background: radial-gradient(ellipse at 50% 50%, var(--card-dark-center) 0%, var(--card-dark-edge) 100%);
  }
  .card--back {
    top: 650px;
    background: radial-gradient(ellipse at 40% 40%, var(--card-light-center) 0%, var(--card-light-edge) 100%);
  }

  .wordmark {
    position: absolute; display: flex; align-items: center;
    font-family: "Montserrat", sans-serif; font-weight: 500; letter-spacing: 1px;
  }
  .wordmark__square { display: block; background: var(--brand-purple); flex: none; }
  .card--front .wordmark { left: 0; right: 0; top: 146px; gap: 16px; justify-content: center; }
  .card--front .wordmark__square { width: 88px; height: 88px; }
  .card--front .wordmark__name { font-size: 76px; color: var(--ink-white); line-height: 1; }

  .card--back .wordmark { left: 72px; top: 38px; gap: 12px; }
  .card--back .wordmark__square { width: 64px; height: 64px; }
  .card--back .wordmark__name { font-size: 50px; color: var(--ink-grey); line-height: 1; }

  .company {
    position: absolute; left: 0; right: 0; top: 312px; text-align: center;
    font-family: "Montserrat", sans-serif;
  }
  .company__name { font-size: 31px; font-weight: 500; color: var(--ink-white); line-height: 1.1; }
  .company__tagline {
    margin-top: 4px; font-size: 13.5px; font-weight: 600;
    background: linear-gradient(90deg, var(--brand-violet), var(--brand-purple));
    -webkit-background-clip: text; background-clip: text; color: transparent;
  }

  .person {
    position: absolute; left: 71px; top: 186px; width: 285px;
    font-family: "Montserrat", sans-serif; font-weight: 500;
    font-size: 34px; line-height: 1.2; color: var(--ink-grey); letter-spacing: 0.3px;
    white-space: nowrap;
  }
  .divider {
    position: absolute; left: 366px; top: 100px; width: 2px; height: 240px;
    background: linear-gradient(180deg, rgba(0,0,0,0), rgba(0,0,0,0.07), rgba(0,0,0,0));
    box-shadow: 2px 0 6px rgba(0,0,0,0.05);
  }
  .contacts {
    position: absolute; left: 383px; top: 136px; list-style: none;
    font-family: "Open Sans", sans-serif; font-size: 19.5px; color: var(--ink-grey-soft);
  }
  .contacts__item { display: flex; align-items: center; gap: 12px; height: 24px; margin-bottom: 37px; white-space: nowrap; }
  .contacts__icon { width: 24px; height: 24px; flex: none; fill: var(--ink-grey-soft); }
</style>
</head>
<body>
<main class="canvas">
  <section class="card card--front">
    <div class="wordmark">
      <span class="wordmark__square"></span>
      <span class="wordmark__name">QVSW</span>
    </div>
    <div class="company">
      <p class="company__name">Quorvane Systems Worldwide</p>
      <p class="company__tagline">International Subtext, Microbial Protection specialists</p>
    </div>
  </section>

  <section class="card card--back">
    <div class="wordmark">
      <span class="wordmark__square"></span>
      <span class="wordmark__name">QVSW</span>
    </div>
    <p class="person">Derek Holloway</p>
    <span class="divider"></span>
    <ul class="contacts">
      <li class="contacts__item">
        <svg class="contacts__icon" viewBox="0 0 24 24" aria-hidden="true"><path d="M1 5h22v14H1z M3 7v10l6-5z M21 7l-6 5 6 5z M3.5 6.5 12 13l8.5-6.5z M4 18h16l-6.2-5L12 14.4 10.2 13z"/></svg>
        <span>tidyshieldnz@mailbox-example.com</span>
      </li>
      <li class="contacts__item">
        <svg class="contacts__icon" viewBox="0 0 24 24" aria-hidden="true"><path d="M6.6 2.5c.6-.3 1.3-.1 1.6.5l2 3.6c.3.6.1 1.2-.4 1.6l-1.5 1c.9 2.2 2.6 4.2 4.7 5.4l1.2-1.4c.4-.5 1.1-.6 1.6-.3l3.5 2.2c.6.3.8 1 .5 1.6l-1 2c-.5 1-1.6 1.5-2.7 1.2C9.5 18.2 4.8 12.6 3.4 6.6c-.3-1 .2-2 1.1-2.6z"/></svg>
        <span>+64290536218</span>
      </li>
      <li class="contacts__item">
        <svg class="contacts__icon" viewBox="0 0 24 24" aria-hidden="true"><path d="M12 1a11 11 0 1 0 0 22 11 11 0 0 0 0-22zm0 2a9 9 0 0 1 6.5 2.8l-1.8.4-1.4 1.6.6 1.8 2 .3.8 2.6-1.1 2.5-1.6 1.3-.3 2.1A9 9 0 0 1 12 21l.9-2.7-1.2-2.4-2.3-.8-.5-2.2 1.4-1.7-.7-1.6-2.5-.3-1.4-2A9 9 0 0 1 12 3z"/></svg>
        <span>www.qvsw-example.us</span>
      </li>
    </ul>
  </section>
</main>
</body>
</html>
```